Best User Interface concept design for Parlo Messenger application

Abstract: A chat application UI design that is implemented especially to perform social media interactions. We are getting ready to start the built out of the app but will need a UI artist to complete the application. We would like to start working right away on the UI concept design right away. We do not require any code at this venture just some graphical concepts. The app will be built out on both Android and IOS.

General Requirements:

1 Ease of use UX and UI design shall be implemented
2 UI design shall be aesthetically pleasing
3 UI design for android and IOS
4 one single UI that works without issues on both phone and tablets

We would like to see some UI design concepts for the following requirements.

Level 1 Requirements:
1. A Parlo application shall be designed to perform the following functionalities:
1.1. Allow users to subscribe to chat service per subscriptions definition found in level 2 requirements definition.
1.2. Import social media contacts from 3rd party services such as Brindlepost, quorvi, etc. per import definition found in level 2 requirements definition.
1.3. Automatically import phone book contacts if installed on a phone
1.4. Allow users to add or invite their imported contacts to sign up and become a part of their available network contacts per Invite definition found in level 2 requirements definition.

1.11. Application shall make use of a status drawer that holds a list of commonly used status and allows users to send status to other users
1.12. Application shall add the ability to customize the activity Drawer to add activity, message associated with activity, contacts associated with the activity
1.13. Application shall make use of a messaging system for both incoming and outgoing alerts as defined in the level 2 Notification requirements definition
1.14. Application shall incorporate texting service so that users can send and receive texts
1.15 Application shall make use of a settings and preferences tab to

We will give more details to the selected company.

```html
<!DOCTYPE html>
<html lang="en">
<head>
<meta charset="utf-8">
<title>Parlo – Contacts</title>
<link rel="stylesheet" href="https://fonts.googleapis.com/css2?family=Arimo:wght@400;700&display=swap">
<style>
:root{
  --status-bg:#161616;
  --blue-top:#66cdf0;
  --blue-bottom:#259fd4;
  --blue-edge:#1b86b8;
  --tab-active:#f1f1f3;
  --tab-idle:#dadadd;
  --panel:#ececef;
  --row-top:#f4f4f6;
  --row-bottom:#e2e2e6;
  --row-line:#c9c9ce;
  --text-dark:#454549;
  --text-mid:#8a8a8f;
  --text-soft:#a2a2a7;
  --coral:#ef7a5c;
  --coral-top:#f2957c;
  --coral-bottom:#e9684a;
  --badge-dark:#4e4e52;
  --online:#8cc63f;
  --away:#e2cf3c;
  --white:#ffffff;
}
*{box-sizing:border-box;margin:0;padding:0}
html,body{width:802px;height:1200px;overflow:hidden;background:var(--panel)}
body{font-family:"Arimo",Arial,sans-serif;position:relative}
.status-bar{position:absolute;left:0;top:0;width:802px;height:50px;background:var(--status-bg);color:var(--white);font-weight:700;font-size:28px}
.status-bar .carrier{position:absolute;left:14px;top:9px;display:flex;align-items:center;gap:8px}
.status-bar .clock{position:absolute;left:0;right:0;top:9px;text-align:center}
.status-bar .battery{position:absolute;right:12px;top:10px}
.app-header{position:absolute;left:0;top:50px;width:802px;height:116px;border-radius:14px 14px 0 0;background:linear-gradient(var(--blue-top),var(--blue-bottom));border-bottom:2px solid var(--blue-edge)}
.header-btn{position:absolute;top:20px;width:110px;height:78px;border-radius:9px;background:linear-gradient(#3db7e6,#1f95ca);border:2px solid var(--blue-edge);box-shadow:inset 0 1px 0 rgba(255,255,255,.45);display:flex;align-items:center;justify-content:center}
.header-btn.menu{left:19px}
.header-btn.profile{right:18px}
.app-name{position:absolute;left:0;right:0;top:20px;text-align:center;color:var(--white);font-weight:700;font-size:66px;line-height:76px}
.tabs{position:absolute;left:0;top:166px;width:802px;height:93px}
.tab{position:absolute;top:0;height:93px;display:flex;align-items:center;font-weight:700;font-size:38px}
.tab.contacts{left:0;width:400px;background:var(--tab-active);color:var(--text-dark);padding-left:36px;gap:16px}
.tab.recent{left:403px;width:399px;background:var(--tab-idle);color:#8d8d92;padding-left:30px;gap:16px;border-left:3px solid #c3c3c8;border-bottom:2px solid #c6c6cb}
.tab-count{width:44px;height:44px;border-radius:50%;background:var(--coral);color:var(--white);font-size:24px;display:flex;align-items:center;justify-content:center;margin-left:26px}
.search-panel{position:absolute;left:0;top:259px;width:802px;height:141px;background:var(--tab-active);border-bottom:2px solid var(--row-line)}
.search-field{position:absolute;left:38px;top:32px;width:596px;height:80px;background:var(--white);border:2px solid #cfcfd4;border-radius:8px;display:flex;align-items:center;padding-left:20px;gap:18px;font-size:28px;color:#9b9ba0}
.search-go{position:absolute;left:652px;top:32px;width:112px;height:80px;border-radius:8px;background:linear-gradient(#45bdec,#1f96cb);border:2px solid var(--blue-edge);display:flex;align-items:center;justify-content:center}
.contact{position:absolute;left:0;width:802px;height:217px;background:linear-gradient(var(--row-top),var(--row-bottom));border-bottom:2px solid var(--row-line);overflow:hidden}
.contact.selected{background:linear-gradient(var(--coral-top),var(--coral-bottom))}
.avatar{position:absolute;left:38px;top:33px;width:148px;height:150px;border-radius:8px;border:3px solid var(--white);box-shadow:0 1px 3px rgba(0,0,0,.25)}
.presence{position:absolute;left:161px;top:160px;width:28px;height:28px;border-radius:50%;border:3px solid var(--white)}
.presence.online{background:var(--online)}
.presence.away{background:var(--away)}
.contact-name{position:absolute;left:221px;top:38px;font-weight:700;font-size:42px;color:var(--text-dark);white-space:nowrap}
.contact-name .time{font-weight:400;font-size:24px;color:var(--text-mid);margin-left:8px}
.preview{position:absolute;left:221px;top:100px;width:470px;font-size:27px;line-height:38px;color:var(--text-soft);white-space:nowrap}
.contact.selected .preview{color:var(--white)}
.contact.selected .contact-name .time{color:#5c3a30}
.contact.muted .contact-name{color:#a8a8ad}
.chevron{position:absolute;left:730px;top:86px}
.unread{position:absolute;right:0;top:0;width:86px;height:86px}
.unread svg{position:absolute;inset:0}
.unread span{position:absolute;right:8px;top:8px;color:var(--white);font-weight:700;font-size:24px}
</style>
</head>
<body>
<header class="status-bar">
  <div class="carrier">
    <svg width="40" height="20" viewBox="0 0 40 20"><g fill="#fff"><rect x="0" y="14" width="5" height="6"/><rect x="8" y="10" width="5" height="10"/><rect x="16" y="6" width="5" height="14"/><rect x="24" y="3" width="5" height="17"/><rect x="32" y="0" width="5" height="20"/></g></svg>
    CARRIER
  </div>
  <div class="clock">4:20 AM</div>
  <svg class="battery" width="90" height="30" viewBox="0 0 90 30"><circle cx="14" cy="15" r="11" fill="#fff"/><path d="M14 8v8h5" stroke="#161616" stroke-width="2.5" fill="none"/><rect x="37" y="5" width="46" height="20" rx="3" fill="none" stroke="#fff" stroke-width="2.5"/><rect x="41" y="9" width="38" height="12" fill="#fff"/><rect x="84" y="11" width="4" height="8" fill="#fff"/></svg>
</header>

<nav class="app-header">
  <div class="header-btn menu">
    <svg width="44" height="34" viewBox="0 0 44 34"><g fill="#fff"><circle cx="5" cy="5" r="4"/><circle cx="5" cy="17" r="4"/><circle cx="5" cy="29" r="4"/><rect x="13" y="2" width="30" height="6" rx="3"/><rect x="13" y="14" width="30" height="6" rx="3"/><rect x="13" y="26" width="30" height="6" rx="3"/></g></svg>
  </div>
  <div class="app-name">Parlo</div>
  <div class="header-btn profile">
    <svg width="34" height="34" viewBox="0 0 34 34"><circle cx="17" cy="10" r="9" fill="#fff"/><path d="M2 34c0-10 6-14 15-14s15 4 15 14z" fill="#fff"/></svg>
  </div>
</nav>

<div class="tabs">
  <div class="tab contacts">
    <svg width="32" height="34" viewBox="0 0 34 34"><circle cx="17" cy="10" r="9" fill="#4a4a4e"/><path d="M2 34c0-10 6-14 15-14s15 4 15 14z" fill="#4a4a4e"/></svg>
    Contacts<span class="tab-count">1</span>
  </div>
  <div class="tab recent">
    <svg width="38" height="38" viewBox="0 0 38 38"><circle cx="19" cy="19" r="16" fill="none" stroke="#8d8d92" stroke-width="3"/><path d="M19 9v11h8" stroke="#8d8d92" stroke-width="3" fill="none"/></svg>
    Recent
  </div>
</div>

<section class="search-panel">
  <div class="search-field">
    <svg width="38" height="38" viewBox="0 0 38 38"><circle cx="14" cy="14" r="10" fill="none" stroke="#9b9ba0" stroke-width="4"/><path d="M22 22l12 12" stroke="#9b9ba0" stroke-width="6" stroke-linecap="round"/></svg>
    Search...
  </div>
  <div class="search-go">
    <svg width="44" height="34" viewBox="0 0 44 34"><path d="M2 11h20V2l20 15-20 15v-9H2z" fill="#fff"/></svg>
  </div>
</section>

<article class="contact" style="top:400px">
  <div class="avatar" role="img" aria-label="Contact photo of Lena Marsh" style="background:linear-gradient(135deg,#c9d3df,#7e8896)"></div>
  <div class="presence online"></div>
  <div class="contact-name">Lena Marsh<span class="time">10:36 pm</span></div>
  <p class="preview">Lorem ipsum dolor sit amet, con-<br>sectetur adipisicing elit, sed do...</p>
  <svg class="chevron" width="36" height="46" viewBox="0 0 36 46"><path d="M6 4l20 19L6 42" stroke="#4a4a4e" stroke-width="8" fill="none" stroke-linecap="round" stroke-linejoin="round"/></svg>
  <div class="unread"><svg viewBox="0 0 86 86"><path d="M0 0h86v86z" fill="var(--coral)"/></svg><span>8</span></div>
</article>

<article class="contact" style="top:619px">
  <div class="avatar" role="img" aria-label="Contact photo of Owen Pryce" style="background:linear-gradient(#c4786a,#d9d2cc)"></div>
  <div class="presence away"></div>
  <div class="contact-name">Owen Pryce<span class="time">09:15 pm</span></div>
  <p class="preview">Duis aute irure dolor in reprehen-<br>derit in voluptate velit esse...</p>
  <svg class="chevron" width="36" height="46" viewBox="0 0 36 46"><path d="M6 4l20 19L6 42" stroke="#4a4a4e" stroke-width="8" fill="none" stroke-linecap="round" stroke-linejoin="round"/></svg>
  <div class="unread"><svg viewBox="0 0 86 86"><path d="M0 0h86v86z" fill="var(--coral)"/></svg><span>5</span></div>
</article>

<article class="contact selected" style="top:835px">
  <div class="avatar" role="img" aria-label="Contact photo of Dario Kent" style="background:linear-gradient(135deg,#6b5a3e,#1f1a14)"></div>
  <div class="presence online"></div>
  <div class="contact-name">Dario Kent<span class="time">08:45 pm</span></div>
  <p class="preview">Lorem ipsum dolor sit amet, con-<br>sectetur adipisicing elit, sed do...</p>
  <svg class="chevron" width="36" height="46" viewBox="0 0 36 46"><path d="M6 4l20 19L6 42" stroke="#4a4a4e" stroke-width="8" fill="none" stroke-linecap="round" stroke-linejoin="round"/></svg>
  <div class="unread"><svg viewBox="0 0 86 86"><path d="M0 0h86v86z" fill="#ec6a4c"/></svg><span>3</span></div>
</article>

<article class="contact muted" style="top:1052px">
  <div class="avatar" role="img" aria-label="Contact photo of Talia R.Voss" style="background:linear-gradient(135deg,#c8342c,#d9a47c)"></div>
  <div class="contact-name">Talia R.Voss<span class="time">08:12</span></div>
  <p class="preview">Lorem ipsum dolor sit amet, con-<br>sectetur adipisicing elit, sed do...</p>
  <svg class="chevron" width="36" height="46" viewBox="0 0 36 46"><path d="M6 4l20 19L6 42" stroke="#4a4a4e" stroke-width="8" fill="none" stroke-linecap="round" stroke-linejoin="round"/></svg>
  <div class="unread"><svg viewBox="0 0 86 86"><path d="M0 0h86v86z" fill="var(--badge-dark)"/></svg><span>14</span></div>
</article>
</body>
</html>
```